Im open to ideas.. I was thinking on my business cards aswell as my logo. a place for my name. email. phone number and abn..

ive attched a file with my business logo. which i dont love the colours.. i was think a dark background with charcoal letters so something along those colour schumes but im open to ideas..

Business

BRL Constructions

```html
<!DOCTYPE html>
<html lang="en">
<head>
<meta charset="utf-8">
<title>BRL Constructions – Business Cards</title>
<link href="https://fonts.googleapis.com/css2?family=PT+Sans:wght@400;700&display=swap" rel="stylesheet">
<style>
  :root {
    --stage: #5b5b5b;
    --card: #000000;
    --accent: #e3161d;
    --sand: #c8bfae;
    --ink-light: #d9d4cb;
  }
  * { box-sizing: border-box; margin: 0; padding: 0; }
  html, body {
    width: 1200px; height: 1200px; overflow: hidden;
    background: var(--stage);
    font-family: "PT Sans", sans-serif;
  }
  .stage { position: relative; width: 1200px; height: 1200px; }
  .card {
    position: absolute; left: 306px; width: 587px; height: 332px;
    background: var(--card);
  }
  .card--front { top: 238px; }
  .card--back { top: 629px; }

  .brand { position: absolute; display: flex; align-items: center; gap: 12px; }
  .brand__mark { width: 14px; height: 14px; background: var(--accent); }
  .brand__name {
    color: var(--sand); font-weight: 700; line-height: 1;
  }
  .brand__main { display: block; font-size: 50px; letter-spacing: 1px; }
  .brand__sub { display: block; font-size: 11px; letter-spacing: 8.5px; margin-top: 4px; text-transform: uppercase; }

  .card--front .brand { left: 31px; top: 62px; }
  .card--back .brand { left: 50%; top: 104px; transform: translateX(-50%); }

  .holder__bar { position: absolute; left: 0; top: 203px; width: 11px; height: 37px; background: var(--accent); }
  .holder__name { position: absolute; left: 32px; top: 198px; color: var(--accent); font-size: 21px; }
  .holder__role { position: absolute; left: 32px; top: 225px; color: var(--ink-light); font-size: 14.5px; }

  .contact { position: absolute; left: 30px; top: 261px; list-style: none; }
  .contact li { display: flex; align-items: center; gap: 7px; color: var(--ink-light); font-size: 14.5px; line-height: 19px; }
  .contact svg { width: 12px; height: 12px; fill: var(--accent); }

  .abn { position: absolute; right: 36px; top: 281px; font-size: 14.5px; color: var(--ink-light); }
  .abn__label { color: var(--accent); }

  .web { position: absolute; left: 0; right: 0; top: 290px; text-align: center; color: var(--sand); font-size: 14.5px; }
</style>
</head>
<body>
<main class="stage">
  <section class="card card--front">
    <div class="brand">
      <span class="brand__mark"></span>
      <span class="brand__name">
        <span class="brand__main">BRL</span>
        <span class="brand__sub">Constructions</span>
      </span>
    </div>
    <span class="holder__bar"></span>
    <p class="holder__name">Sam Carter</p>
    <p class="holder__role">Managing Partner</p>
    <ul class="contact">
      <li>
        <svg viewBox="0 0 12 12" aria-hidden="true"><path d="M1 3h10v7H1z M1 3l5 4 5-4" fill="var(--accent)"/><path d="M1.5 3.5l4.5 3.5 4.5-3.5" stroke="#000" stroke-width="1" fill="none"/></svg>
        sam@brlbuild.com
      </li>
      <li>
        <svg viewBox="0 0 12 12" aria-hidden="true"><path d="M1 4.5C1 2.5 3 2 6 2s5 .5 5 2.5v.8H8.5V4H3.5v1.3H1z"/><path d="M3 6.5h6l1 4H2z"/><circle cx="6" cy="8.3" r="1.1" fill="#000"/></svg>
        000.000.0000
      </li>
    </ul>
    <p class="abn"><span class="abn__label">ABN</span> #0000000</p>
  </section>

  <section class="card card--back">
    <div class="brand">
      <span class="brand__mark"></span>
      <span class="brand__name">
        <span class="brand__main">BRL</span>
        <span class="brand__sub">Constructions</span>
      </span>
    </div>
    <p class="web">www.brlbuild.com</p>
  </section>
</main>
</body>
</html>
```